All Natural Raw Honey & Goats Milk Body Wash Labels

We have launched a new product line of all natural Raw Honey & Goats Milk body wash with the business name being Dawn Meadow and the tag line Naturally . Their are currently three line items requiring three labels. Natural (Unscented), Japanese Honeysuckle and Caribbean.
It is a family orientated product that we want to promote as being all natural, healthy and trustworthy. It is an all Australian made product that uses our very own award winning raw honey
I can supply the file for the business name/logo upon request

Target Market(s)

Families

Industry/Entity Type

Bath & body

Requirements
Must have
• a Lux high end feel
Nice to have
• simple easy to read with minimal images
Should not have
• No cartoons

```html
<!DOCTYPE html>
<html lang="en">
<head>
<meta charset="utf-8">
<title>Natural – Raw Honey &amp; Goats Milk Body Wash Label</title>
<link rel="stylesheet" href="https://fonts.googleapis.com/css2?family=Cinzel:wght@400&family=Arimo:wght@700&display=swap">
<style>
  :root {
    --page: #f4f4f2;
    --label-top: #e9eae3;
    --label-bottom: #dfe0d2;
    --rule: #b9b8a2;
    --comb: #f3f3ee;
    --ink-grey: #8b8b84;
    --ink-gold: #b0a987;
  }
  html, body {
    margin: 0;
    width: 1053px;
    height: 1200px;
    overflow: hidden;
    background: var(--page);
  }
  .label {
    position: absolute;
    left: 76px;
    top: 233px;
    width: 900px;
    height: 734px;
    background: linear-gradient(180deg, var(--label-top), var(--label-bottom));
    overflow: hidden;
  }
  .label__rule {
    position: absolute;
    left: 0;
    right: 0;
    height: 3px;
    background: var(--rule);
  }
  .label__rule--top { top: 4px; }
  .label__rule--bottom { top: 700px; }
  .label__honeycomb {
    position: absolute;
    left: 150px;
    top: 10px;
    width: 600px;
    height: 250px;
    background: radial-gradient(ellipse at 50% 30%, var(--comb), rgba(243,243,238,0) 70%);
  }
  .label__product-line {
    position: absolute;
    top: 104px;
    left: 0;
    right: 0;
    margin: 0;
    text-align: center;
    font-family: "Arimo", Arial, sans-serif;
    font-weight: 700;
    font-size: 26px;
    letter-spacing: -0.3px;
    color: var(--ink-grey);
  }
  .label__variant {
    position: absolute;
    top: 262px;
    left: 0;
    right: 0;
    margin: 0;
    text-align: center;
    font-family: "Cinzel", "Times New Roman", serif;
    font-weight: 400;
    font-size: 112px;
    line-height: 1;
    letter-spacing: 2px;
    color: var(--ink-gold);
  }
  .label__brand {
    position: absolute;
    top: 528px;
    left: 0;
    right: 0;
    margin: 0;
    text-align: center;
    font-family: "Cinzel", "Times New Roman", serif;
    font-weight: 400;
    font-size: 34px;
    letter-spacing: 3px;
    color: var(--ink-grey);
  }
  .label__brand-dot {
    display: inline-block;
    width: 12px;
    height: 12px;
    margin-right: 14px;
    border-radius: 50%;
    background: var(--ink-grey);
    vertical-align: middle;
  }
</style>
</head>
<body>
  <section class="label">
    <div class="label__rule label__rule--top"></div>
    <div class="label__honeycomb" role="img" aria-label="Faint honeycomb pattern"></div>
    <p class="label__product-line">NATURAL RAW HONEY &amp; GOATS MILK BODY WASH</p>
    <h1 class="label__variant">NATURAL</h1>
    <p class="label__brand"><span class="label__brand-dot"></span>Dawn Meadow</p>
    <div class="label__rule label__rule--bottom"></div>
  </section>
</body>
</html>
```